I want a double sided flyer possibly with a picture of a lawn or grass.
Company name, phone number, email, and logo
Halvorsen Turf Management, (404)726-1853,Halvorsen_Turf@brevimail.com
Company services
Fertilization and weed control,Lawn and Landscape maintenance, mowing, pruning, aeration, landscape and Christmas lights,

```html
<!DOCTYPE html>
<html lang="en">
<head>
<meta charset="utf-8">
<title>Halvorsen Turf Management – Flyer</title>
<link href="https://fonts.googleapis.com/css2?family=Arimo:wght@400;700&display=swap" rel="stylesheet">
<style>
  :root {
    --canvas-bg: #ece9e4;
    --brand-green: #2f9a3f;
    --deep-green: #1f7a2c;
    --bright-green: #49b84a;
    --grass-light: #7fc35a;
    --grass-mid: #4fa53a;
    --grass-dark: #2e7f2a;
    --white: #ffffff;
    --haze: #f4f5f2;
  }
  * { box-sizing: border-box; margin: 0; padding: 0; }
  html, body { width: 1200px; height: 1000px; overflow: hidden; }
  body {
    background: var(--canvas-bg);
    font-family: "Arimo", Arial, sans-serif;
    position: relative;
  }
  .flyer-side {
    position: absolute;
    top: 32px;
    width: 416px;
    height: 875px;
    overflow: hidden;
    box-shadow: 0 4px 14px rgba(0,0,0,0.18);
  }
  .flyer-front { left: 158px; }
  .flyer-back { left: 616px; }

  /* Front */
  .front-photo {
    position: absolute; inset: 0;
    background: linear-gradient(180deg,
      var(--haze) 0%, var(--haze) 30%,
      #e6ebe2 45%, #b9d4a4 62%,
      var(--grass-light) 78%, var(--grass-mid) 100%);
  }
  .brand {
    position: absolute;
    top: 60px; left: 0; right: 0;
    text-align: center;
  }
  .brand-dot {
    display: block;
    width: 86px; height: 86px;
    margin: 0 auto 34px;
    border-radius: 50%;
    background: var(--brand-green);
  }
  .brand-name {
    color: var(--brand-green);
    font-weight: 700;
    font-size: 30px;
    line-height: 1.15;
  }
  .contact {
    position: absolute;
    left: 0; right: 0;
    text-align: center;
    color: var(--white);
    font-weight: 700;
  }
  .contact-phone {
    top: 752px;
    font-size: 50px;
    letter-spacing: -0.5px;
    text-shadow: 0 0 3px var(--deep-green), 0 0 3px var(--deep-green);
  }
  .contact-email {
    top: 830px;
    font-size: 22px;
    text-shadow: 0 0 3px var(--deep-green), 0 0 3px var(--deep-green);
  }

  /* Back */
  .back-photo {
    position: absolute; inset: 0;
    background: linear-gradient(170deg,
      var(--grass-light) 0%, var(--grass-mid) 40%,
      #3f9a34 65%, var(--grass-dark) 100%);
  }
  .wave { position: absolute; left: 0; width: 416px; }
  .wave-top { top: 0; }
  .wave-bottom { bottom: 0; }
  .services {
    position: absolute;
    top: 176px; left: 0; right: 0;
    text-align: center;
    color: var(--white);
    text-shadow: 0 2px 4px rgba(0,0,0,0.35);
  }
  .services-title {
    font-size: 36px;
    font-weight: 400;
    margin-bottom: 42px;
  }
  .services-list { list-style: none; }
  .services-list li {
    font-size: 32px;
    line-height: 46px;
  }
</style>
</head>
<body>
  <section class="flyer-side flyer-front">
    <div class="front-photo" role="img" aria-label="Photo of a lawnmower wheel on fresh green grass with a soft blurred background"></div>
    <div class="brand">
      <span class="brand-dot"></span>
      <p class="brand-name">Halvorsen Turf<br>Management</p>
    </div>
    <p class="contact contact-phone">(404)726-1853</p>
    <p class="contact contact-email">Halvorsen_Turf@brevimail.com</p>
  </section>

  <section class="flyer-side flyer-back">
    <div class="back-photo" role="img" aria-label="Photo of a freshly mowed striped green lawn"></div>
    <svg class="wave wave-top" width="416" height="110" viewBox="0 0 416 110">
      <path d="M0,0 H416 V42 C340,30 270,78 180,82 C110,85 50,62 0,70 Z" fill="#2f9a3f"/>
      <path d="M0,76 C50,68 110,92 180,88 C270,84 340,36 416,48" fill="none" stroke="#ffffff" stroke-width="5"/>
    </svg>
    <h2 class="services">
      <span class="services-title" style="display:block">Company services:</span>
      <ul class="services-list">
        <li>Fertilization and weed</li>
        <li>control</li>
        <li>Lawn and Landscape</li>
        <li>maintenance</li>
        <li>mowing</li>
        <li>pruning</li>
        <li>aeration</li>
        <li>landscape</li>
        <li>Christmas lights</li>
      </ul>
    </h2>
    <svg class="wave wave-bottom" width="416" height="110" viewBox="0 0 416 110">
      <path d="M0,110 H416 V24 C340,16 270,52 180,40 C110,30 50,10 0,14 Z" fill="#3aa844"/>
      <path d="M0,8 C50,4 110,24 180,34 C270,46 340,10 416,18" fill="none" stroke="#ffffff" stroke-width="5"/>
    </svg>
  </section>
</body>
</html>
```